Standee design for an exhibition event

"Please read the details carefully:

80 cm (W) X 200 cm (H)
Res: 150dpi
output file : ai file.
Corporate Health Checkups
- Companies understand the importance of executive wellness for their employees. An unfit and unhealthy employee loses his productivity due to frequent absenteeism, lack of concentration and low energy levels at work. Regular health screening is the key to good employee health management.

```html
<!DOCTYPE html>
<html lang="en">
<head>
<meta charset="utf-8">
<title>Corporate Health Checkups – Standee</title>
<link rel="stylesheet" href="https://fonts.googleapis.com/css2?family=Arimo:ital,wght@0,400;0,700;1,400;1,700&display=swap">
<style>
  :root {
    --brand-green: #0b7357;
    --ink-grey: #4a4a4a;
    --band-grey: #555a5c;
    --paper: #ffffff;
    --photo-warm: #b8927a;
    --photo-cool: #d9dde2;
    --photo-deep: #3a3430;
  }
  * { margin: 0; padding: 0; box-sizing: border-box; }
  html, body {
    width: 1200px;
    height: 2397px;
    overflow: hidden;
    background: var(--paper);
    font-family: "Arimo", Arial, sans-serif;
  }
  .standee {
    position: relative;
    width: 1200px;
    height: 2397px;
    overflow: hidden;
    background: var(--brand-green);
  }
  .header {
    position: absolute;
    inset: 0 0 auto 0;
    height: 430px;
  }
  .header-shape {
    position: absolute;
    inset: 0;
    width: 1200px;
    height: 430px;
  }
  .brand {
    position: absolute;
    top: 100px;
    left: 0;
    right: 0;
    text-align: center;
  }
  .brand-name {
    display: block;
    font-weight: 700;
    font-size: 106px;
    line-height: 1;
    letter-spacing: -2px;
    color: var(--brand-green);
  }
  .brand-tagline {
    display: block;
    margin: 12px 90px 0 0;
    text-align: right;
    font-weight: 700;
    font-style: italic;
    font-size: 40px;
    color: var(--ink-grey);
  }
  .content {
    position: absolute;
    top: 450px;
    left: 80px;
    right: 70px;
    color: var(--paper);
  }
  .headline {
    font-weight: 700;
    font-size: 188px;
    line-height: 0.98;
    letter-spacing: -2px;
  }
  .intro {
    margin-top: 40px;
    font-style: italic;
    font-size: 44px;
    line-height: 1.2;
  }
  .key-message {
    margin-top: 36px;
    font-style: italic;
    font-weight: 700;
    font-size: 48px;
    line-height: 1.2;
  }
  .photo-zone {
    position: absolute;
    left: 0;
    bottom: 0;
    width: 1200px;
    height: 760px;
  }
  .photo-zone svg {
    display: block;
    width: 1200px;
    height: 760px;
  }
</style>
</head>
<body>
<main class="standee">

  <header class="header">
    <svg class="header-shape" viewBox="0 0 1200 430" aria-hidden="true">
      <path d="M0 0 H1200 V360 C1000 330 820 350 600 385 C380 420 180 420 0 395 Z" fill="var(--band-grey)"/>
      <path d="M0 0 H1200 V340 C1000 310 820 330 600 365 C380 400 180 400 0 375 Z" fill="var(--paper)"/>
    </svg>
    <div class="brand">
      <span class="brand-name">HarbourviewHospital</span>
      <span class="brand-tagline">Your Trusted Partner for Health</span>
    </div>
  </header>

  <section class="content">
    <h1 class="headline">Corporate<br>Health<br>Checkups</h1>
    <p class="intro">Companies understand the importance of<br>executive wellness for their employees.<br>An unfit and unhealthy employee loses<br>his productivity due to frequent absenteeism,<br>lack of concentration and low energy levels<br>at work.</p>
    <p class="key-message">Regular health screening is the key to<br>good employee health management.</p>
  </section>

  <div class="photo-zone" role="img" aria-label="Photo of a presenter explaining a health check chart to an audience of employees in a meeting room">
    <svg viewBox="0 0 1200 760" aria-hidden="true">
      <defs>
        <linearGradient id="photoTone" x1="0" y1="0" x2="0.4" y2="1">
          <stop offset="0" stop-color="var(--photo-cool)"/>
          <stop offset="0.45" stop-color="var(--photo-warm)"/>
          <stop offset="1" stop-color="var(--photo-deep)"/>
        </linearGradient>
      </defs>
      <path d="M0 190 C180 65 420 10 700 8 C900 6 1080 30 1200 70 V760 H0 Z" fill="var(--band-grey)"/>
      <path d="M0 226 C180 98 420 42 700 40 C900 38 1080 62 1200 100 V760 H0 Z" fill="url(#photoTone)"/>
    </svg>
  </div>

</main>
</body>
</html>
```